Flyer für IT-Dienstleistungen für Privatpersonen
Zielgruppe
IT-Dienstleistungen für Privatpersonen vorwiegened Senioren
Aufgabenstellung
Verwendet werden soll ein DIN A6 Zickzackfalz, Falz Längsseite, Bund Rechts, 6-8Seiten, Matt, Beschnittzugabe 1mm, Sicherheitsabstand 4mm, Farblich und Designtechnisch passend zur Webseite.
Die Textformatierung darf angepasst werden

```html
<!DOCTYPE html>
<html lang="de">
<head>
<meta charset="utf-8">
<title>Datenwacht – Flyer Rückseite und Titelseite</title>
<link href="https://fonts.googleapis.com/css2?family=Lato:wght@300;400;700&family=Montserrat:wght@600&display=swap" rel="stylesheet">
<style>
  :root {
    --stage: #333333;
    --panel-top: #133219;
    --panel-bottom: #0a1a0d;
    --green: #3fa24d;
    --green-light: #5cc065;
    --text: #ffffff;
  }
  * { margin: 0; padding: 0; box-sizing: border-box; }
  html, body {
    width: 1200px; height: 800px; overflow: hidden;
    background: var(--stage);
    font-family: "Lato", Arial, sans-serif;
  }
  .flyer-page {
    position: absolute;
    top: 69px;
    width: 470px; height: 662px;
    background: linear-gradient(170deg, var(--panel-top) 0%, var(--panel-bottom) 100%);
    overflow: hidden;
    box-shadow: 0 18px 40px rgba(0,0,0,.45);
    color: var(--text);
  }
  .flyer-back { left: 115px; }
  .flyer-front { left: 615px; }

  /* Rückseite */
  .benefits { position: absolute; left: 56px; right: 48px; top: 180px; }
  .benefits-title {
    font-family: "Montserrat", Arial, sans-serif;
    font-weight: 600; font-size: 30px; letter-spacing: 1px;
    margin-bottom: 30px;
  }
  .benefit { margin-bottom: 28px; }
  .benefit-name {
    color: var(--green-light);
    font-size: 21px; font-weight: 400; line-height: 1.25;
  }
  .benefit-text {
    font-size: 18px; font-weight: 400; line-height: 1.35;
    padding-left: 14px;
  }

  /* Titelseite */
  .flyer-front .artwork { position: absolute; inset: 0; width: 100%; height: 100%; }
  .brand {
    position: absolute; top: 62px; left: 0; right: 0;
    display: flex; align-items: center; justify-content: center; gap: 11px;
    font-size: 27px; font-weight: 400; letter-spacing: 3px; text-transform: uppercase;
  }
  .brand-dot { width: 20px; height: 20px; border-radius: 50%; background: var(--green); }
  .claim {
    position: absolute; left: 50px; right: 34px; top: 520px;
    font-size: 19px; font-weight: 700; line-height: 1.55;
    letter-spacing: .3px;
  }
  .claim-line { display: block; text-align: justify; text-align-last: justify; }
  .claim-line.last { text-align: left; text-align-last: left; }
  .claim .highlight {
    color: var(--green-light);
    font-size: 32px; font-weight: 300; letter-spacing: 1px; line-height: 1;
  }
  .claim .accent { color: var(--green-light); }
</style>
</head>
<body>
  <section class="flyer-page flyer-back">
    <div class="benefits">
      <h2 class="benefits-title">Warum wir?</h2>
      <div class="benefit">
        <p class="benefit-name">Ehrlich und transparent</p>
        <p class="benefit-text">was Sie vorher sehen, ist der Preis.</p>
      </div>
      <div class="benefit">
        <p class="benefit-name">Non-Profit Gedanke</p>
        <p class="benefit-text">ohne Gewinn als oberstes Ziel.</p>
      </div>
      <div class="benefit">
        <p class="benefit-name">Verständlich</p>
        <p class="benefit-text">einfach erklärt, ohne Fachchinesisch.</p>
      </div>
      <div class="benefit">
        <p class="benefit-name">Vor Ort</p>
        <p class="benefit-text">Sie bleiben bequem zu Hause.</p>
      </div>
    </div>
  </section>

  <section class="flyer-page flyer-front">
    <svg class="artwork" viewBox="0 0 511 720" preserveAspectRatio="none">
      <defs>
        <linearGradient id="swoosh-fill" x1="0" y1="0" x2="1" y2="1">
          <stop offset="0" stop-color="#47ad55"/>
          <stop offset="1" stop-color="#1e6b2a"/>
        </linearGradient>
        <radialGradient id="ring-fill" cx="0.5" cy="0.5" r="0.5">
          <stop offset="0.78" stop-color="#2e8a3a"/>
          <stop offset="1" stop-color="#46ae54"/>
        </radialGradient>
        <radialGradient id="photo-fill" cx="0.55" cy="0.45" r="0.6">
          <stop offset="0" stop-color="#f4f7f8"/>
          <stop offset="0.6" stop-color="#d9e3e6"/>
          <stop offset="1" stop-color="#b8c6c9"/>
        </radialGradient>
      </defs>
      <path class="swoosh" fill="url(#swoosh-fill)"
        d="M0 180 C70 178 140 182 195 186 C170 196 150 206 135 218
           C95 255 78 305 78 355 C78 420 105 475 160 515
           C200 528 230 532 250 535 C180 548 120 575 85 620
           C55 655 35 690 25 720 L0 720 Z"/>
      <circle cx="295" cy="350" r="185" fill="#0d2411" opacity=".7"/>
      <circle cx="300" cy="345" r="172" fill="url(#ring-fill)"/>
      <circle cx="300" cy="345" r="138" fill="url(#photo-fill)"
        role="img" aria-label="Foto: Hand tippt auf einer Laptop-Tastatur, darüber vernetzte Symbole"/>
    </svg>

    <div class="brand"><span class="brand-dot"></span>Datenwacht</div>

    <p class="claim">
      <span class="claim-line">Ob Computer, Smartphone &amp; Tablet –</span>
      <span class="claim-line">mit uns haben Sie einen Partner an</span>
      <span class="claim-line last">Ihrer Seite, der <span class="highlight">ALLES</span> für Sie regelt<span class="accent">.</span></span>
    </p>
  </section>
</body>
</html>
```